Assessment Report cover design and formatting

This report is for senior executives and provides leaders with detailed insight into their capabilities and skills. The cover should have space for the date and name of the person doing the assessment. We are looking to modernise the report cover design. We would like the report to be our company colours if possible. The work will likely expand once the cover is done to other parts of the report, ie. the format and layout of the report etc.

Company colours:
Primary colours:
• Blue #0D47A1, #115CD0, #90B6ED, #EEf3FB
• Green #0D91A1, #47A10D, #324C196, #0DA11D
Additional colours:
• Purple #A10D91
• Brown #A1670D
• Red #A10D47

Target Market(s)

Executives

Industry/Entity Type

Consulting, leadership development

Colors
0094D4
00A9DD
6FCCEA
C7EBF8
E9F6FB
00AB8E
00BBA5
67D7C9
C6EFE9
E9F9F6
E54698
E96AAD
F1A4CE
F9D9EA
FCEFF6
6B429C
8869AF
B7A5CE
E3DAEB
F3F0F8

Requirements
Must have
• The report cover should have space for name of user, the date and company logo. Cover should be in A4 size.

```html
<!DOCTYPE html>
<html lang="en">
<head>
<meta charset="utf-8">
<title>Summit Executive Review – Insight Report Cover</title>
<link rel="stylesheet" href="https://fonts.googleapis.com/css2?family=Montserrat:wght@300;400;500;700;800&display=swap">
<style>
  :root {
    --backdrop: #7d7d7d;
    --paper: #ffffff;
    --paper-tint: #f1f3f6;
    --blue-deep: #1d45a6;
    --blue-mid: #115cd0;
    --blue-light: #5f86d6;
    --teal: #1cb4d3;
    --green: #2fb56b;
    --ink: #333a45;
  }
  * { margin: 0; padding: 0; box-sizing: border-box; }
  html, body { width: 1200px; height: 840px; overflow: hidden; }
  body {
    background: var(--backdrop);
    font-family: "Montserrat", Arial, sans-serif;
    display: flex;
    align-items: center;
    justify-content: center;
  }
  .cover {
    position: relative;
    width: 566px;
    height: 800px;
    background: linear-gradient(180deg, var(--paper) 60%, var(--paper-tint) 100%);
    overflow: hidden;
    box-shadow: 0 10px 30px rgba(0,0,0,.3);
  }
  .cover-art { position: absolute; inset: 0; width: 566px; height: 800px; }

  .series-title {
    position: absolute;
    top: 92px;
    right: 48px;
    padding-right: 14px;
    border-right: 2px solid var(--blue-deep);
    text-align: right;
    text-transform: uppercase;
    line-height: 1;
  }
  .series-title .kicker { display: block; font-size: 21px; font-weight: 500; color: var(--blue-deep); letter-spacing: 1px; }
  .series-title .lead { display: block; font-size: 44px; font-weight: 800; color: var(--green); margin-top: 6px; letter-spacing: 1px; }
  .series-title .main { display: block; font-size: 31px; font-weight: 800; color: var(--blue-deep); margin-top: 6px; }

  .brand {
    position: absolute;
    top: 548px;
    left: 40px;
    display: flex;
    align-items: center;
    gap: 8px;
    font-size: 19px;
    font-weight: 700;
    color: var(--blue-deep);
  }
  .brand-dot { width: 12px; height: 12px; border-radius: 50%; background: var(--teal); }

  .report-heading {
    position: absolute;
    top: 600px;
    right: 46px;
    text-align: right;
    text-transform: uppercase;
    line-height: 1.05;
  }
  .report-heading .insight { display: block; font-size: 34px; font-weight: 500; color: var(--green); letter-spacing: 1px; }
  .report-heading .for { display: block; font-size: 38px; font-weight: 800; color: var(--blue-deep); }
  .report-meta {
    position: absolute;
    top: 690px;
    right: 46px;
    text-align: right;
    font-size: 16px;
    font-weight: 400;
    color: var(--blue-light);
    line-height: 1.3;
  }

  .sign-fields {
    position: absolute;
    left: 40px;
    bottom: 28px;
    width: 300px;
    font-size: 11px;
    color: var(--ink);
  }
  .sign-field { display: flex; align-items: flex-end; gap: 8px; margin-top: 12px; }
  .sign-field .rule { flex: 1; border-bottom: 1px solid var(--ink); height: 1px; }
</style>
</head>
<body>
  <main class="cover">
    <svg class="cover-art" viewBox="0 0 566 800">
      <defs>
        <linearGradient id="photoTone" x1="0" y1="1" x2="1" y2="0">
          <stop offset="0" stop-color="#1a3f63"/>
          <stop offset="0.45" stop-color="#3f8fae"/>
          <stop offset="1" stop-color="#d3ecf3"/>
        </linearGradient>
        <linearGradient id="bandTone" x1="0" y1="0" x2="1" y2="0">
          <stop offset="0" stop-color="#1d45a6"/>
          <stop offset="0.5" stop-color="#115cd0"/>
          <stop offset="0.8" stop-color="#1cb4d3"/>
          <stop offset="1" stop-color="#3fbf8a"/>
        </linearGradient>
      </defs>

      <path role="img" aria-label="Photograph: executive in a suit looking over a night city skyline, blended in a double exposure"
            fill="url(#photoTone)"
            d="M0,0 H566 V480 L0,360 Z"/>

      <path class="accent-band" fill="url(#bandTone)"
            d="M0,360 L566,480 L566,514 L0,392 Z"/>
    </svg>

    <h1 class="series-title">
      <span class="kicker">Summit</span>
      <span class="lead">Executive</span>
      <span class="main">Review</span>
    </h1>

    <div class="brand"><span class="brand-dot"></span>Northfield Partners</div>

    <h2 class="report-heading">
      <span class="insight">Insight</span>
      <span class="for">Report for:</span>
    </h2>
    <p class="report-meta">Sample<br>22 August 2023</p>

    <div class="sign-fields">
      <div class="sign-field"><span>Name:</span><span class="rule"></span></div>
      <div class="sign-field"><span>Date:</span><span class="rule"></span></div>
    </div>
  </main>
</body>
</html>
```